Flyer for a Unique Type of Tax Services

Please refer to the attached sample design for reference. Feel free to change the wording as needed. Here is the project brief:

Objective:
Objective of this flyer is to introduce our services which we are launching soon, which is new of a kind, to our potential customers i.e. online tax return preparation. By looking at the flyer we want our target audience to get convinced of our services and visit our website and register with us. They don’t have to pay anything to register.

Our Competitors:
Currently there are three main options available to get tax returns prepared. First is to buy tax software and get tax return prepared at own, this is the cheapest option. There are studies that suggest that people who are not well aware of tax laws there are chances they miss certain tax refunds by filing returns at their own and potentially lose money. Second option is to go to the local offices of nation-wide tax service companies like Pell & Varne and Morrow Tandy. They open offices only during tax season i.e. Jan through April but they are not available other part of the year and their association with the customers is temporary. Third option is to go to a CPA office which are the most expensive and very few people go for this option.

Weaknesses of the Current Options:
By self-preparing tax returns, there are chances that one can overlook certain tax laws that can provide additional tax credits and exemptions to people and overall they could have got a higher tax refund from the Govt. but they may miss it.
By going to other competitors during the peak time when tax returns are due, there are high chances that they don't have enough time to do research to ensure maximum refunds based on the exact circumstances of the individuals at the peak time as many people come to them during that time. Also they are not available after the tax season to provide them any answers to their questions or provide them tax planning tips to help them save tax in the next season.
By going to the CPA office, they charge a lot of fees and also for any tax advice later during the year, they will charge additional fees.

What we are offering:
We are offering a new option i.e. online tax return preparation through experts. We'll charge the fees competitive to what people are paying to local tax providers. But we will be different than our competitors as we'll be providing value added service if they got their returns prepared through us. Value added services we will be free of any additional cost for our customers who'll get tax return prepared through us.

Our Target Audience:
Our target audience is any person or couple who go to the tax service providers like Pell & Varne or Morrow Tandy to get their tax returns prepared.

How We are Different:
Here is the summary of the unique aspects of our business as compared to the competitors:
- Customers just pay us the price for preparing the annual return and price is comparable and competitive to what they have been paying to other providers.
- Unlike our competitors, we do extensive research to review the circumstances of our customers and explore applicable tax laws to make sure all available tax credits, exemptions, and deductions are taken for our customers, whereas our customers don't usually do such kind of research as during the peak tax season when customers approach them they usually don’t have time to do that kind of research. We start our association with our customers much sooner than the actual due date and this provides us time to do extensive research and we try our best that our customers could get higher tax returns.
- By just getting tax returns prepared through us, we enter into a long-term association with our customers and provide them complimentary tax planning tips throughout the year to help them save tax in the following year
- We are available to our customers year-round to provide complementary answers to any tax related questions without any additional cost e.g. how to save tax when buying a car, whether to buy or lease the care to save tax, for the sole-proprietor business how to save tax by using portion of the home as home-office, how to save tax by using personal car for personal business.
- We also provide answers to other basic financial advise related matters e.g. which insurance product is better, whether full insurance or term-life insurance to chose, how to save for the retirement etc.

Other Details:
Our logo has already been designed and we want the same logo to be used in the flyer. Our website address is: www.FiledRightPlus.com (it is still under construction but to get perspective of what we are trying to offer, visit this alternate website that it not final yet but will give an idea: http://www.filedrightplus.com/wordpress. Fyi, a video at this link is only a placeholder and not relevant to our services)

Requirements
Must have
• Please refer to the sample flyer attached. Feel free to change the design and language.
Should not have
• Please do not put any testimonial on the flyer as reflected in the under construction website.

```html
<!DOCTYPE html>
<html lang="en">
<head>
<meta charset="utf-8">
<title>FiledRight Plus – Tax Services Flyer</title>
<link href="https://fonts.googleapis.com/css2?family=Open+Sans:wght@400;600;700&display=swap" rel="stylesheet">
<style>
  :root {
    --backdrop: #e6e7e9;
    --paper: #f7f7f8;
    --orange: #ee7a2e;
    --orange-deep: #e06a1f;
    --blue: #3b6fb6;
    --ink: #4a4d52;
    --ink-soft: #5c6066;
    --photo-top: #c9d3df;
    --photo-mid: #3c4f72;
    --photo-low: #eef1f5;
    --edge: #3a3c40;
  }
  * { box-sizing: border-box; margin: 0; padding: 0; }
  html, body { width: 1200px; height: 800px; overflow: hidden; }
  body {
    background: var(--backdrop);
    font-family: "Open Sans", Arial, sans-serif;
    color: var(--ink);
  }
  .flyer {
    position: absolute;
    left: 330px; top: 16px;
    width: 540px; height: 768px;
    background: var(--paper);
    border-bottom: 5px solid var(--edge);
    box-shadow: 0 6px 18px rgba(0,0,0,.18);
    overflow: hidden;
  }
  .hero-photo {
    height: 168px;
    background: linear-gradient(160deg, var(--photo-low) 0%, var(--photo-top) 35%, var(--photo-mid) 70%, #2a3957 100%);
    border-bottom: 4px solid var(--orange);
  }
  .brand {
    text-align: center;
    margin-top: 18px;
    font-size: 32px;
    line-height: 1.25;
    font-weight: 700;
    color: var(--blue);
    letter-spacing: 1px;
  }
  .brand-dot {
    display: block;
    width: 12px; height: 12px;
    margin: 6px auto 0;
    border-radius: 50%;
    background: var(--orange);
  }
  .questions {
    list-style: none;
    margin: 16px 48px 0 56px;
    font-size: 14px;
    line-height: 1.35;
  }
  .questions li {
    position: relative;
    padding-left: 22px;
    margin-bottom: 7px;
  }
  .questions li svg {
    position: absolute; left: 0; top: 4px;
  }
  .hl { color: var(--blue); font-weight: 700; }
  .offer-band {
    margin-top: 16px;
    background: linear-gradient(90deg, var(--orange-deep), var(--orange));
    color: #fff;
    text-align: center;
    font-size: 20px;
    line-height: 1.3;
    padding: 12px 36px;
  }
  .register {
    text-align: center;
    margin-top: 20px;
    font-size: 22px;
    line-height: 1.3;
    font-weight: 400;
    letter-spacing: 1px;
    color: var(--ink);
  }
  .site-url {
    text-align: center;
    margin-top: 2px;
    font-size: 17px;
    color: var(--orange);
  }
  .closing {
    text-align: center;
    margin: 12px 34px 0;
    font-size: 13.5px;
    line-height: 1.4;
    color: var(--ink-soft);
  }
</style>
</head>
<body>
  <article class="flyer">
    <div class="hero-photo" role="img" aria-label="Photo of business professionals in suits reviewing documents at a desk"></div>

    <div class="brand">FILEDRIGHT PLUS<span class="brand-dot"></span></div>

    <ul class="questions">
      <li>
        <svg width="12" height="12" viewBox="0 0 12 12"><path d="M1 1l4 5-4 5M6 1l4 5-4 5" fill="none" stroke="#ee7a2e" stroke-width="2"/></svg>
        Does your tax Return Preparer has time to do Extensive Research has to do <span class="hl">Extensive Research</span> for you to help you get <span class="hl">maximum refunds</span>?
      </li>
      <li>
        <svg width="12" height="12" viewBox="0 0 12 12"><path d="M1 1l4 5-4 5M6 1l4 5-4 5" fill="none" stroke="#ee7a2e" stroke-width="2"/></svg>
        Do you get year-round <span class="hl">Free Advice</span> regarding your <span class="hl">Tax related Questions</span> from your exiting Tax Service Provider?
      </li>
      <li>
        <svg width="12" height="12" viewBox="0 0 12 12"><path d="M1 1l4 5-4 5M6 1l4 5-4 5" fill="none" stroke="#ee7a2e" stroke-width="2"/></svg>
        Does youe existing Tax Servise Provider give you <span class="hl">Complementary Tax Planning Tips</span> throught the year to help you <span class="hl">save tax in the following year</span>?
      </li>
    </ul>

    <p class="offer-band">If not, then try us as we do provide all these year - round to our customers who get tax returns prepared through us at no additional cost.</p>

    <h2 class="register">REGISTER NOW FREE AT</h2>
    <p class="site-url">www.FiledRightPlus.com</p>

    <p class="closing">And right away we'll start doing research for you and will be available year-round to answer your tax related questions and will keep providing you tax planning tips and also provide you guideline on other financial planning matters.</p>
  </article>
</body>
</html>
```